BUilding Fascia Signage

I got the logo, now, I want to design the Fascia Signage for my shop.
Fasica signage is 5565mm x 470mmH
Need idea how to put the logo, text, colour to the fascia signage.
need something catching.
can add more decorate line.
may try with Black background and white background

Design & Build

```html
<!DOCTYPE html>
<html lang="en">
<head>
<meta charset="utf-8">
<title>RVN Building Group – Fascia Signage</title>
<link href="https://fonts.googleapis.com/css2?family=Russo+One&display=swap" rel="stylesheet">
<style>
  :root {
    --backdrop: #bdbdbd;
    --sign-black: #050505;
    --sign-blue: #3a86f0;
    --sign-white: #ffffff;
  }
  html, body {
    margin: 0;
    padding: 0;
    width: 1200px;
    height: 778px;
    overflow: hidden;
    background: var(--backdrop);
  }
  .canvas {
    position: relative;
    width: 1200px;
    height: 778px;
  }
  .fascia-sign {
    position: absolute;
    left: 22px;
    top: 340px;
    width: 1156px;
    height: 98px;
    box-shadow: 0 3px 8px rgba(0, 0, 0, 0.25);
  }
  .fascia-sign text {
    font-family: "Russo One", sans-serif;
  }
  .brand-name { fill: var(--sign-white); }
  .tagline { fill: var(--sign-blue); }
  .panel-black { fill: var(--sign-black); }
  .accent-blue { fill: var(--sign-blue); }
  .panel-white { fill: var(--sign-white); }
</style>
</head>
<body>
<main class="canvas">
  <svg class="fascia-sign" viewBox="0 0 1445 122" role="img" aria-label="RVN Building Group fascia sign: Your home our heart crafted to Lumea">
    <rect class="panel-black" x="0" y="0" width="1445" height="122"/>
    <polygon class="accent-blue" points="250,0 1445,0 1445,14 246,14"/>
    <polygon class="accent-blue" points="250,0 270,0 232,122 212,122"/>
    <rect class="accent-blue" x="0" y="116" width="220" height="6"/>
    <polygon class="panel-white" points="272,28 1445,28 1445,122 242,122"/>

    <g class="brand-lockup">
      <text class="brand-name" x="98" y="72" font-size="38" text-anchor="middle">RVN</text>
      <text class="brand-name" x="98" y="94" font-size="13" text-anchor="middle" letter-spacing="0.5">BUILDING GROUP</text>
    </g>

    <text class="tagline" x="302" y="95" font-size="46" textLength="1107" lengthAdjust="spacingAndGlyphs">YOUR HOME OUR HEART CRAFTED TO LUMEA</text>
  </svg>
</main>
</body>
</html>
```